Website banners + icons

Hello,

For our website www.tolvarmeadow.com who is a very serious website for immigration, integration and naturalisation in Switzerland, we need :

3 x homepage banners : 998px/300px
10 x banners : 998px/150px (concerns the website pages)
icons 24px/24px

The idea is to present a black/white banners with the current text and the theme must be in accordance with the page title.

The graphic line must be very clean and including some fine red informations or line or what ever but very clean and design full.

Please do not use stereotypes like hand shakes...

We are also open to work with abstract things or art.

We let your creativity works on.

Good luck

```html
<!DOCTYPE html>
<html lang="en">
<head>
<meta charset="utf-8">
<title>Integration – Local Regulation Guidance</title>
<link rel="stylesheet" href="https://fonts.googleapis.com/css2?family=Syncopate&display=swap">
<style>
  :root {
    --ink-white: #ffffff;
    --accent-red: #e3120b;
    --panel-tint: rgba(20, 20, 20, 0.78);
    --photo-light: #bdbdbd;
    --photo-mid: #7a7a7a;
    --photo-dark: #262626;
  }
  html, body {
    margin: 0;
    padding: 0;
    width: 1200px;
    height: 361px;
    overflow: hidden;
    background: var(--photo-dark);
  }
  .banner {
    position: relative;
    width: 1200px;
    height: 361px;
    overflow: hidden;
    font-family: "Syncopate", sans-serif;
  }
  .banner__photo {
    position: absolute;
    inset: 0;
    background:
      linear-gradient(160deg, rgba(0,0,0,0) 0%, rgba(0,0,0,0) 42%, rgba(20,20,20,0.85) 58%, rgba(30,30,30,0.9) 100%),
      linear-gradient(180deg, var(--photo-light) 0%, var(--photo-mid) 45%, var(--photo-dark) 100%);
  }
  .banner__panel {
    position: absolute;
    left: 681px;
    top: 162px;
    width: 499px;
    height: 181px;
    background: var(--panel-tint);
  }
  .banner__title {
    position: absolute;
    left: 38px;
    top: 24px;
    margin: 0;
    color: var(--ink-white);
    font-weight: 400;
    font-size: 40px;
    line-height: 1;
    letter-spacing: 0.08em;
    white-space: nowrap;
  }
  .banner__subtitle {
    position: absolute;
    left: 38px;
    top: 110px;
    margin: 0;
    color: var(--accent-red);
    font-weight: 400;
    font-size: 23px;
    line-height: 39px;
    letter-spacing: 0.06em;
    white-space: nowrap;
  }
</style>
</head>
<body>
  <div class="banner">
    <div class="banner__photo" role="img" aria-label="Black and white aerial view of an old town with tall houses lining a river and a small bridge"></div>
    <div class="banner__panel">
      <h1 class="banner__title">Integration</h1>
      <p class="banner__subtitle">Local Regulation<br>Guidance</p>
    </div>
  </div>
</body>
</html>
```